Business Consulting Website Design

UPDATED KEY MESSAGES:

The client has decided o a different direction.

The Key Messages include:
-- Creating something unique.
Every company is unique, ever culture unique. Every project customized to meet the unique needs of the client. No two things are alike.
-- One of a kind
Because every company is different, every culture is different, every objective is unique
-- Customized solutions
We create something just for you …

I think the approach needs to be about creating a masterpiece as opposed to nurturing/growing.

Perhaps we could have different abstract/colorful paint items that takes up part of the page for each landing page. Against white and on the white is where we put our text.

Client also has created a Pixelgrove Lightbox with images that she likes

http://www.pixelgrove-example.com/public_board.mhtml?code=a7c2e9f04b8d13562e7f90a1c4d6b852&board_id=58217409

She also likes the watercolor look against white background.

===============================
Need a Homepage and an Interior page redesign for my client: http://www.brightwavecounsel-example.com

Client does leadership development, performance management, talent development, etc. Has some great clients.

- This site is very old and needs a modern look. Update look & colors. She wants simple but not bland.
- Banner images should be interesting.
- She likes the purple in her logo
- She thinks Arial font is outdated and boring
- We will be rewriting all the copy.
- Design should include ProLinker icon, phone, email, and address
- She likes the client grid on the Our Clients page. We will be redoing this.

- Menus will include:
-- Home
-- What We Do
-- Who We Are
-- Our Clients
-- Snapshots (these are case studies)

One of the sites she liked is http://lanternfold-novel-example.com, though this website has much more content than she will have.

I'm attaching the following files for your reference:
- Her new business card proof that contains her logo
- a zip file containing some stock image comps

Need strong design. Site will likely be built in Wordpress.

Thanks,
Nora
Updates

Target Market(s)

SVP of Human Resources or Head of Talent

Industry/Entity Type

Business

Number of Pages Required

2 page

Font styles to use
Sans Serif

Colors
b768aa
876aae
6b449b
f04a50
f37122

Requirements
Must have
• - Designer must read the brief
• - Use logo
Nice to have
• - Strong banner images to complement the key message
• - Design will function work on mobile easily
Should not have
• - Should not look like a design template was purchased from layoutbazaar-example.com or other template sites.
• - Should not be too masculine
• - Should not feel cluttered.

```html
<!DOCTYPE html>
<html lang="en">
<head>
<meta charset="utf-8">
<title>Brightwave Counsel</title>
<link href="https://fonts.googleapis.com/css2?family=Open+Sans:wght@300;400;600;700&family=Josefin+Sans:wght@400;600&display=swap" rel="stylesheet">
<style>
  :root{
    --page:#f7f7f7;
    --white:#ffffff;
    --purple:#4b2283;
    --violet:#6b449b;
    --lavender:#876aae;
    --orchid:#b768aa;
    --teal:#1f8275;
    --orange:#f37122;
    --coral:#f04a50;
    --ink:#333333;
    --body:#555555;
    --rule:#e4e4e4;
    --button:#6d6d6d;
  }
  *{box-sizing:border-box;margin:0;padding:0}
  html,body{width:761px;height:1200px;overflow:hidden}
  body{background:var(--page);font-family:"Open Sans",Arial,sans-serif;color:var(--body);position:relative}
  a{text-decoration:none}

  .brand{position:absolute;left:0;right:0;text-align:center;font-family:"Josefin Sans",sans-serif;font-weight:600;color:var(--violet);letter-spacing:4px;line-height:1.15}
  .brand .mark{display:block;margin:0 auto 8px;width:16px;height:16px;background:var(--violet)}
  .site-brand{top:26px;font-size:20px}

  .nav{position:absolute;left:96px;top:136px;width:569px;height:29px;background:var(--purple);display:flex;padding-left:46px}
  .nav a{color:var(--white);font-size:10.5px;font-weight:700;letter-spacing:.2px;display:flex;align-items:center;justify-content:center;border-left:1px solid rgba(255,255,255,.18)}
  .nav a:last-child{border-right:1px solid rgba(255,255,255,.18)}

  .hero{position:absolute;left:96px;top:166px;width:569px;height:236px;background:var(--white);overflow:hidden}
  .hero .wash{position:absolute;inset:0;background:
      radial-gradient(ellipse 150px 110px at 110px 90px, rgba(183,104,170,.75), rgba(183,104,170,0) 70%),
      radial-gradient(ellipse 130px 100px at 200px 160px, rgba(243,113,34,.6), rgba(243,113,34,0) 70%),
      radial-gradient(ellipse 120px 90px at 60px 190px, rgba(240,74,80,.55), rgba(240,74,80,0) 70%),
      radial-gradient(ellipse 140px 100px at 250px 60px, rgba(135,106,174,.6), rgba(135,106,174,0) 70%),
      radial-gradient(ellipse 90px 70px at 300px 200px, rgba(107,68,155,.45), rgba(107,68,155,0) 70%)}
  .hero h1{position:absolute;left:332px;top:70px;color:var(--violet);font-weight:400;font-size:28px;line-height:32px;letter-spacing:3px}
  .hero .dots{position:absolute;left:255px;top:218px;display:flex;gap:10px}
  .hero .dots span{width:6px;height:6px;border-radius:50%;background:rgba(107,68,155,.3)}
  .hero .dots span:first-child{background:var(--violet)}

  .intro{position:absolute;left:96px;top:408px;width:569px;height:260px;background:var(--white)}
  .intro h2{text-align:center;font-weight:300;color:var(--lavender);font-size:22px;margin-top:14px}
  .feature{position:absolute;top:72px;width:136px}
  .feature svg{display:block;width:30px;height:30px;margin:0 0 14px 48px}
  .feature h3{font-weight:400;font-size:13.5px;margin-bottom:8px;white-space:nowrap}
  .feature p{font-size:9px;line-height:12.5px;color:var(--ink)}
  .f1{left:5px}.f1 h3{color:var(--orchid)}
  .f2{left:146px}.f2 h3{color:var(--violet)}
  .f3{left:290px}.f3 h3{color:var(--teal)}
  .f4{left:433px}.f4 h3{color:var(--orange)}

  .section-title{position:absolute;left:0;right:0;top:694px;text-align:center;font-weight:300;font-size:21px;color:var(--lavender)}

  .testimonial{position:absolute;top:740px;width:176px;height:200px}
  .testimonial .client{height:50px;display:flex;align-items:center;justify-content:center;gap:6px;font-weight:700;font-size:12px;color:var(--ink)}
  .testimonial .client i{width:14px;height:14px;display:block}
  .testimonial h4{font-size:9px;font-weight:700;color:var(--ink);line-height:11px;margin:20px 0 4px}
  .testimonial p{font-size:8.5px;line-height:11.5px;color:var(--ink);display:-webkit-box;-webkit-box-orient:vertical;-webkit-line-clamp:7;overflow:hidden}
  .testimonial .more{position:absolute;top:188px;left:0;font-size:7px;font-weight:700;color:var(--ink);text-decoration:underline}
  .testimonial .more b{color:var(--orange)}
  .t1{left:104px}.t2{left:300px}.t3{left:491px}
  .divider{position:absolute;top:742px;width:1px;height:200px;background:var(--rule)}

  .button{position:absolute;left:292px;top:973px;width:178px;height:22px;background:var(--button);color:var(--white);font-size:9.5px;font-weight:700;display:flex;align-items:center;justify-content:center;gap:6px}

  .footer{position:absolute;left:96px;top:1022px;width:569px;height:116px;background:var(--white)}
  .footer .brand{left:0;right:auto;width:192px;top:28px;font-size:13px;letter-spacing:3px}
  .footer .brand .mark{width:11px;height:11px;margin-bottom:6px}
  .contact{position:absolute;left:160px;width:246px;top:26px;text-align:center;font-size:7.5px;line-height:11px;color:var(--ink)}
  .contact strong{display:block;font-size:8px;margin-bottom:6px}
  .contact span{display:block;margin-bottom:5px}
  .social{position:absolute;left:420px;width:130px;top:26px;text-align:center;font-size:8px;color:var(--ink)}
  .social strong{display:block;margin-bottom:10px}
  .social ul{list-style:none;font-size:8px;font-weight:600;color:var(--violet);line-height:12px}
  .copyright{position:absolute;left:0;right:0;top:1148px;text-align:center;font-size:6.5px;color:var(--ink)}
</style>
</head>
<body>
  <div class="brand site-brand"><span class="mark"></span>BRIGHTWAVE<br>COUNSEL</div>

  <nav class="nav">
    <a href="#" style="width:72px">HOME</a>
    <a href="#" style="width:110px">WHAT WE DO</a>
    <a href="#" style="width:92px">WHO WE ARE</a>
    <a href="#" style="width:96px">OUR CLIENTS</a>
    <a href="#" style="width:96px">SNAPSHOTS</a>
  </nav>

  <section class="hero">
    <div class="wash" role="img" aria-label="Abstract colourful watercolour paint wash spreading across a white background"></div>
    <h1>Create your<br>Masterpiece</h1>
    <div class="dots"><span></span><span></span><span></span><span></span></div>
  </section>

  <section class="intro">
    <h2>An invaluable partner to your company and employees.</h2>
    <div class="feature f1">
      <svg viewBox="0 0 30 30" fill="#b768aa"><circle cx="15" cy="8" r="5"/><circle cx="6" cy="11" r="3.5"/><circle cx="24" cy="11" r="3.5"/><path d="M7 26c0-6 3.5-10 8-10s8 4 8 10z"/><path d="M0 25c0-5 2.5-8 6-8 1 0 2 .3 2.5.7C6.5 20 6 22.5 6 25z"/><path d="M30 25c0-5-2.5-8-6-8-1 0-2 .3-2.5.7C23.5 20 24 22.5 24 25z"/></svg>
      <h3>Experience counts</h3>
      <p>Experience in developing and implementing programs, materials, and communications that meet all of your human resource requirements. Whether you need to create programs from scratch, or review, revise and update your current programs.</p>
    </div>
    <div class="feature f2">
      <svg viewBox="0 0 30 30" fill="#6b449b"><circle cx="11" cy="18" r="7"/><g stroke="#6b449b" stroke-width="3"><path d="M11 8v20M1 18h20M4 11l14 14M18 11L4 25"/></g><circle cx="11" cy="18" r="2.5" fill="#fff"/><circle cx="23" cy="8" r="4.5"/><g stroke="#6b449b" stroke-width="2"><path d="M23 2v12M17 8h12"/></g><circle cx="23" cy="8" r="1.5" fill="#fff"/></svg>
      <h3>Exceptional service</h3>
      <p>We strive to give you exceptional service, with extraordinary attention to detail, providing unique solutions to meet each project's objective.</p>
    </div>
    <div class="feature f3">
      <svg viewBox="0 0 30 30" fill="none" stroke="#1f8275" stroke-width="2.5"><path d="M2 2v26h27"/><path d="M6 22l7-8 5 5 9-10"/><path d="M21 8h6v6"/></svg>
      <h3>On time. On budget.</h3>
      <p>Because we understand the human resource demands of business today, we are able to produce and implement your programs efficiently, cost-effectively, and in a time-sensitive manner.</p>
    </div>
    <div class="feature f4">
      <svg viewBox="0 0 30 30" stroke="#f37122" stroke-width="2.5" fill="#f37122"><path d="M3 6h24M3 15h24M3 24h24"/><rect x="17" y="3" width="4" height="6"/><rect x="8" y="12" width="4" height="6"/><rect x="19" y="21" width="4" height="6"/></svg>
      <h3>Your resource</h3>
      <p>Whether your company is small, large, or somewhere in between - with ongoing human resource needs or specific projects - Brightwave Counsel is your one resource to rely on for comprehensive program development... every step of the way.</p>
    </div>
  </section>

  <h2 class="section-title">Testemonials</h2>

  <article class="testimonial t1">
    <div class="client"><i style="background:var(--coral)"></i>Northpeak Office Group</div>
    <h4>Brightwave Counsel forges long-term relationships.</h4>
    <p>"Northpeak Office Group has turned to Brightwave Counsel on many occasions over the last seven years for assistance in developing our management and leadership learning continuum, as well as consulting on a myriad of high-impact human resource initiatives. Miriam's experience, design prowess and...</p>
    <a class="more" href="#">READ MORE <b>›</b></a>
  </article>
  <div class="divider" style="left:286px"></div>
  <article class="testimonial t2">
    <div class="client"><i style="background:var(--orange);border-radius:50%"></i>Tilehaven</div>
    <h4>Brightwave Counsel helps fast growing companies grow fast!</h4>
    <p>How do you help a company that is growing at a pace of 40% growth per year? Very quickly! That's exactly what Brightwave Counsel did for Tilehaven. Read what the President of the company had to say about his experience with Brightwave Counsel.</p>
    <a class="more" href="#">READ MORE <b>›</b></a>
  </article>
  <div class="divider" style="left:475px"></div>
  <article class="testimonial t3">
    <div class="client"><i style="background:#8a1f2c"></i>Copyline Supplies</div>
    <h4>Copyline Supplies recommends Brightwave Counsel.</h4>
    <p>"Miriam is an exceptional blend of HR talent and analytical skill ..... While providing us with possible solutions to the issues impacting our company, Miriam provided a very well organized and customized guidebook for our employees. Her penetrating clarity has vastly improved our internal business...</p>
    <a class="more" href="#">READ MORE <b>›</b></a>
  </article>

  <a class="button" href="#">MORE TESTIMONIALS <svg width="8" height="10" viewBox="0 0 8 10"><path d="M2 1l4 4-4 4" stroke="#fff" stroke-width="2" fill="none"/></svg></a>

  <footer class="footer">
    <div class="brand"><span class="mark"></span>BRIGHTWAVE<br>COUNSEL</div>
    <div class="contact">
      <strong>Miriam Ellsworth Hale, Principal</strong>
      <span>office 555.201.0144</span>
      <span>82 Larkspur Court NE<br>Marlow, Georgia 30999</span>
      <span>Miriam@BrightwaveCounsel-example.com</span>
    </div>
    <div class="social">
      <strong>Social Media:</strong>
      <ul><li>ProLinker</li><li>Facepage</li><li>Circlenet</li></ul>
    </div>
  </footer>

  <p class="copyright">Copyright © 2003-2015 Brightwave Counsel, Inc.</p>
</body>
</html>
```